****Business Card Design for Quillmark Development. Design based around attached logo/company name

I’m looking for business card design for my company Quillmark Development Group,LLC. Design should be professional, sharp and minimal. Outside of the attached logos, greyscale colors for remainder of cards. My thoughts are two-sided card with attached logo on one side and my info on the other but open to one-sided as well with right design.
Target Market(s)
Real estate professionals including banks, private investors, property owners, developers, commercial tenants like Brewmoor, Varnell or Tasker’s.
Industry/Entity Type
Commercial real estate development and investments.
Contact Information for Business Card
Name, title, email, phone #’s, web address and physical address
Font styles to use
Other font styles liked:
- Helvetica, Garamond, etc
Colors
Designer to choose only greyscale colors for use in the design.
Requirements
Must have
- Attached logo first or second options.
Nice to have
- Two sided card with logo on one side. Attached Logo/company name can be laid out any way that flows as long as it’s legible.name
Should not have
- No loud colors. ***Please do not include logo, I have removed the company design with a logo image.

```html
<!DOCTYPE html>
<html lang="en">
<head>
<meta charset="UTF-8">
<title>Quillmark Development Group, LLC — Business Card</title>
<link rel="stylesheet" href="https://fonts.googleapis.com/css2?family=Montserrat:wght@300;400;700&display=swap">
<style>
  :root {
    --backdrop: #d6d6d6;
    --card: #5b6272;
    --ink: #ffffff;
    --ink-soft: #e4e6ea;
    --divider: #c9ccd3;
  }
  * { box-sizing: border-box; margin: 0; padding: 0; }
  html, body {
    width: 1200px; height: 913px; overflow: hidden;
    background: var(--backdrop);
  }
  .stage {
    width: 1200px; height: 913px;
    display: flex; align-items: center; justify-content: center; gap: 40px;
  }
  .card {
    width: 540px; height: 309px;
    background: var(--card);
    position: relative;
    color: var(--ink);
    font-family: "Montserrat", Arial, sans-serif;
  }
  .identity {
    position: absolute; left: 16px; top: 92px; width: 240px;
    text-align: right;
  }
  .identity__name {
    font-weight: 700; font-size: 22px; letter-spacing: 0.2px; line-height: 1.1;
    text-transform: uppercase; white-space: nowrap;
  }
  .identity__title {
    font-weight: 300; font-size: 14px; margin-top: 6px; color: var(--ink-soft);
    white-space: nowrap;
  }
  .divider {
    position: absolute; left: 272px; top: 80px; width: 1px; height: 80px;
    background: var(--divider);
  }
  .contacts {
    position: absolute; left: 292px; top: 82px; list-style: none;
  }
  .contacts li {
    display: flex; align-items: center; gap: 9px;
    font-weight: 300; font-size: 13px; line-height: 26px; color: var(--ink-soft);
    white-space: nowrap;
  }
  .contacts svg, .address svg { width: 13px; height: 13px; flex: none; fill: var(--ink); }
  .contacts .icon-globe { fill: none; stroke: var(--ink); stroke-width: 2; }
  .address {
    position: absolute; left: 0; right: 0; bottom: 52px;
    display: flex; justify-content: center; align-items: center; gap: 9px;
    font-weight: 300; font-size: 14px; color: var(--ink-soft);
    white-space: nowrap;
  }
  .brand {
    position: absolute; inset: 0;
    display: flex; align-items: center; justify-content: center; gap: 12px;
    font-weight: 400; font-size: 22px; color: var(--ink-soft);
    white-space: nowrap;
  }
  .brand__mark { width: 14px; height: 14px; background: var(--ink-soft); flex: none; }
</style>
</head>
<body>
<main class="stage">
  <section class="card card--info">
    <div class="identity">
      <h1 class="identity__name">Elliot Harwood</h1>
      <p class="identity__title">Managing Director</p>
    </div>
    <div class="divider"></div>
    <ul class="contacts">
      <li><svg viewBox="0 0 24 24" aria-hidden="true"><path d="M6.6 10.8a15 15 0 0 0 6.6 6.6l2.2-2.2a1 1 0 0 1 1-.25 11.4 11.4 0 0 0 3.6.57 1 1 0 0 1 1 1V20a1 1 0 0 1-1 1A17 17 0 0 1 3 4a1 1 0 0 1 1-1h3.5a1 1 0 0 1 1 1c0 1.25.2 2.45.57 3.57a1 1 0 0 1-.25 1z"/></svg>044-987 654 321</li>
      <li><svg viewBox="0 0 24 24" aria-hidden="true"><path d="M2 5h20v14H2zm2 2v.5l8 5 8-5V7l-8 5z"/></svg>info@quillmarkdev.com</li>
      <li><svg class="icon-globe" viewBox="0 0 24 24" aria-hidden="true"><circle cx="12" cy="12" r="9"/><ellipse cx="12" cy="12" rx="4" ry="9"/><path d="M3 12h18"/></svg>www.quillmarkdev.com</li>
    </ul>
    <p class="address"><svg viewBox="0 0 24 24" aria-hidden="true"><path d="M12 2a7 7 0 0 0-7 7c0 5 7 13 7 13s7-8 7-13a7 7 0 0 0-7-7zm0 9.5A2.5 2.5 0 1 1 12 6.5a2.5 2.5 0 0 1 0 5z"/></svg>118, Harbour Row Eastfield, 30418</p>
  </section>
  <section class="card card--brand">
    <div class="brand">
      <span class="brand__mark" aria-hidden="true"></span>
      <p class="brand__name">Quillmark Development Group, LLC</p>
    </div>
  </section>
</main>
</body>
</html>
```